BRIGHT COLORFUL + 55 FAMILY HISTORY BROCHURE 11 x 17 bifold

11 x 17 Bifold Flyer I have given you the Layout I just need you to make it Pretty

YOU DO NOT NEED TO FOLLOW MY LAYOUT, You can but dont have too

Target Market(s)

55 year old consumers, who could choose our service of Hereditary Cancer Screening

Industry/Entity Type

Health And Wellness

Requirements
Must have
• Must be appealing to Grand Parents, must make them want to test , show lots of pictures of grand children, YOU DO NOT NEED TO FOLLOW MY LAYOUT , You can but dont have too
Nice to have
• use our colors of our logo , YOU DO NOT NEED TO FOLLOW MY LAYOUT , You can but dont have too
Should not have
• YOU DO NOT NEED TO FOLLOW MY LAYOUT, You can but dont have too

```html
<!DOCTYPE html>
<html lang="en">
<head>
<meta charset="utf-8">
<title>Hereditary Cancer Screening – Bifold Brochure</title>
<link rel="stylesheet" href="https://fonts.googleapis.com/css2?family=Raleway:wght@400;500;600;700;800&display=swap">
<style>
  :root {
    --lime: #7dfc00;
    --lime-text: #7ee81a;
    --navy: #0b1766;
    --navy-text: #1a2472;
    --ink: #111111;
    --paper: #ffffff;
    --backdrop: #e9eaec;
  }
  * { box-sizing: border-box; margin: 0; padding: 0; }
  html, body { width: 1200px; height: 1014px; overflow: hidden; }
  body {
    background: var(--backdrop);
    font-family: "Raleway", Arial, sans-serif;
    position: relative;
  }
  .spread {
    position: absolute;
    left: 60px; top: 157px;
    width: 1080px; height: 700px;
    display: flex;
    box-shadow: 0 18px 40px rgba(0,0,0,.18);
  }
  .page { position: relative; width: 540px; height: 700px; overflow: hidden; }

  /* Left page */
  .page-inside { background: var(--paper); }
  .top-band { position: absolute; left: 0; top: 0; width: 100%; height: 70px; background: var(--lime); }
  .photo { position: absolute; }
  .photo-grandparents {
    left: 0; top: 22px; width: 400px; height: 200px;
    background: linear-gradient(135deg, #c9ccd4 0%, #e8dccd 45%, #b9c7e0 100%);
  }
  .headline {
    position: absolute; right: 30px; top: 234px;
    color: var(--navy-text); font-weight: 500; font-size: 19px; line-height: 1.3;
    text-align: right; white-space: nowrap;
  }
  .photo-grandma {
    left: 300px; top: 298px; width: 210px; height: 122px;
    background: linear-gradient(135deg, #6e4a35 0%, #c58a62 50%, #8aa3c8 100%);
  }
  .lead {
    position: absolute; left: 40px; top: 302px; width: 245px;
    color: var(--lime-text); font-weight: 600; font-size: 16px; line-height: 1.3;
  }
  .body-copy {
    position: absolute; left: 40px; top: 442px; width: 470px;
    color: var(--ink); font-size: 12.5px; line-height: 1.35; font-weight: 500;
  }
  .body-copy strong { font-weight: 800; }
  .brand {
    position: absolute; left: 150px; top: 552px;
    display: flex; align-items: center; gap: 12px;
  }
  .brand-dot { width: 44px; height: 44px; border-radius: 50%; background: var(--navy); }
  .brand-name { color: var(--navy); font-weight: 700; font-size: 20px; letter-spacing: .04em; }
  .bottom-band {
    position: absolute; left: 0; bottom: 0; width: 100%; height: 70px; background: var(--lime);
    display: flex; align-items: center; justify-content: center;
  }
  .url { color: var(--navy); font-size: 15px; font-weight: 500; }

  /* Right page */
  .page-cover { background: var(--navy); }
  .cover-title-band {
    position: absolute; left: 0; top: 0; width: 100%; height: 48px; background: var(--lime);
    display: flex; align-items: center; justify-content: center;
  }
  .cover-title { color: var(--navy); font-size: 22px; font-weight: 500; }
  .tagline {
    position: absolute; top: 60px; width: 100%; text-align: center;
    color: var(--lime-text); font-size: 17px; font-weight: 400;
  }
  .photo-hands {
    left: 0; top: 92px; width: 540px; height: 200px;
    background: linear-gradient(90deg, #0b1766 0%, #5a6ea8 22%, #c79a7e 45%, #e2b597 60%, #6d9fd6 85%, #0b1766 100%);
  }
  .question {
    position: absolute; top: 300px; width: 100%; text-align: center;
    color: var(--paper); font-size: 17px; line-height: 1.3;
  }
  .photo-strip { position: absolute; left: 14px; top: 370px; width: 512px; height: 76px; display: flex; gap: 4px; }
  .photo-strip .thumb { flex: 1; height: 100%; }
  .thumb-1 { background: linear-gradient(135deg, #e9d6c9, #9bb3d6); }
  .thumb-2 { background: linear-gradient(135deg, #d8b08b, #7a6a5c); }
  .thumb-3 { background: linear-gradient(135deg, #6b4a38, #c69a7a); }
  .thumb-4 { background: linear-gradient(135deg, #8a6a55, #d2ae90); }
  .thumb-5 { background: linear-gradient(135deg, #7fbf5a, #c4c9d2); }
  .thumb-6 { background: linear-gradient(135deg, #d9c0ad, #8f7a6c); }
  .gift {
    position: absolute; top: 480px; width: 100%; text-align: center;
    color: var(--paper); font-size: 19px;
  }
  .knowing {
    position: absolute; top: 530px; width: 100%; text-align: center;
    color: var(--lime-text); font-size: 19px; line-height: 1.3;
  }
  .knowing strong { display: block; font-weight: 800; }
  .cover-bottom-band {
    position: absolute; left: 0; bottom: 0; width: 100%; height: 62px; background: var(--lime);
    display: flex; align-items: center; justify-content: center;
  }
</style>
</head>
<body>
  <main class="spread">
    <section class="page page-inside">
      <div class="top-band"></div>
      <div class="photo photo-grandparents" role="img" aria-label="Photo of grandparents hugging and kissing their young grandchild"></div>
      <h2 class="headline">DOES CANCER Run in Your Family?<br>A Simple Swab Could SAVE a Family Members LIFE</h2>
      <div class="photo photo-grandma" role="img" aria-label="Photo of a smiling grandmother being kissed by two grandchildren"></div>
      <p class="lead">Your decision won't just affect you. It will also impact Your Family, since your test results may Forecast Their Cancer Risks, too.</p>
      <p class="body-copy"><strong>We believe it is important to understand what can and cannot be learned with genetic testing.</strong> Genetic mutations can increase risks for certain cancers, but this does not mean cancer will definitely develop. You should be prepared to receive positive or negative results. <strong>Most people receive Negative Results meaning no mutations associated with an increased risk for the Hereditary cancers.</strong></p>
      <div class="brand">
        <span class="brand-dot"></span>
        <span class="brand-name">KINWELL HEALTH GROUP</span>
      </div>
      <footer class="bottom-band"><span class="url">www.kinwellscreening.com</span></footer>
    </section>

    <section class="page page-cover">
      <header class="cover-title-band"><h1 class="cover-title">Hereditary Cancer Screening</h1></header>
      <p class="tagline">The Test You Take For Them</p>
      <div class="photo photo-hands" role="img" aria-label="Photo of a grandparent's hand holding a child's small hand by one finger"></div>
      <p class="question">Will You give Your loved ones the<br>information to Beat Cancer in their lives ?</p>
      <div class="photo-strip">
        <div class="thumb thumb-1" role="img" aria-label="Photo of grandmother with granddaughter"></div>
        <div class="thumb thumb-2" role="img" aria-label="Photo of smiling grandfather with child"></div>
        <div class="thumb thumb-3" role="img" aria-label="Photo of grandmother hugging grandchild"></div>
        <div class="thumb thumb-4" role="img" aria-label="Photo of grandfather with granddaughter"></div>
        <div class="thumb thumb-5" role="img" aria-label="Photo of grandfather hugging young boy"></div>
        <div class="thumb thumb-6" role="img" aria-label="Photo of grandmother embracing granddaughter"></div>
      </div>
      <p class="gift">Give Them the Gift of Knowledge</p>
      <p class="knowing">knowing is better than not knowing.<strong>Knowledge is Power</strong></p>
      <footer class="cover-bottom-band"><span class="url">www.kinwellscreening.com</span></footer>
    </section>
  </main>
</body>
</html>
```